beauty salon application for consumer

- Find your favorite beauty salons and spas or discover new places next to you with geolocation;
- Filter your search by price, distance, category and type of service;
- Never worry again about having to schedule during your work hours or about not having your calls answered when you want to book an appointment;
- Mark salons as favorites and be the first to be informed of exclusive discounts;
- Don’t ever forget your appointments with Glow Slot’s notifications;
- Compare prices, places and services freely, in a quick and practical way;
- Share reviews about services and places you go with other users and read their opinions;
- USER-FRIENDLY INTERFACE
- GALLERY
- OFFERS

similar interface with application name "pamperlane"

Industry/Entity Type

Beauty Salon

Font styles to use
Decorative
Script

Colors

Designer to choose colors to be used in the design.

Requirements
Must have
• Please have a look into these applications:
• 1- https://apps.example-store.test/gb/app/pamperlane/id572913804/?pid=korvasa&c=footer-link
• 2- https://apps.example-store.test/us/app/curlo-ltd-book-curl-style-glam-polish-services/id3948172065
• 3- https://market.sample-apps.test/store/apps/details?id=com.parlorvix.user&hl=en
• 4- https://apps.example-store.test/app/id463187209?mt=8
Nice to have
• Nice to give me a clear screenshots for main function of the application ,please see the above applications before giving me a design .

```html
<!DOCTYPE html>
<html lang="en">
<head>
<meta charset="utf-8">
<title>pamperlane – salon booking screens</title>
<link href="https://fonts.googleapis.com/css2?family=Hind:wght@300;400;500&family=Inter:wght@500;600&display=swap" rel="stylesheet">
<style>
:root{
  --bg-top:#f3f2fb;
  --bg-bottom:#ffffff;
  --screen:#f2eff9;
  --card:#ffffff;
  --ink:#2f2f36;
  --muted:#55555e;
  --line:#6a6a72;
  --accent:#7b5cf5;
  --teal:#1b9aa2;
  --star:#f6c019;
  --mint:#e3f2ec;
  --marker:#1f6ff2;
}
*{box-sizing:border-box;margin:0;padding:0}
html,body{width:1200px;height:800px;overflow:hidden}
body{font-family:"Hind",sans-serif;color:var(--ink);
  background:linear-gradient(var(--bg-top) 0,var(--bg-top) 466px,var(--bg-bottom) 466px);position:relative}
.phone{position:absolute;top:82px;width:360px;height:640px;background:var(--screen);overflow:hidden;
  box-shadow:0 6px 22px rgba(90,80,140,.12);border-radius:4px}
.phone--dashboard{left:30px}
.phone--menu{left:420px}
.phone--booking{left:802px}
.abs{position:absolute}
.status{position:absolute;top:0;left:0;right:0;height:22px;font-family:"Inter",sans-serif;font-size:11px;font-weight:600;color:#111;z-index:5}
.status__time{position:absolute;left:0;right:0;text-align:center;top:5px}
.status__left{position:absolute;left:6px;top:5px}
.status__right{position:absolute;right:8px;top:5px;display:flex;gap:4px;align-items:center}
.avatar{position:absolute;top:24px;left:322px;width:30px;height:30px;border-radius:50%;
  background:radial-gradient(circle at 50% 40%,#c79a80,#5a3a2c);border:2px solid #fff;z-index:5}
/* dashboard */
.dash-map{left:0;top:0;width:360px;height:278px;
  background:linear-gradient(180deg,var(--mint) 0,#e8f0ec 30%,#e4e8e6 60%,#e9ebea 100%)}
.marker{position:absolute;width:8px;height:8px;border-radius:50%;background:var(--marker)}
.marker--me{width:12px;height:12px;box-shadow:0 0 0 15px rgba(31,111,242,.2)}
.hamburger{left:11px;top:34px;z-index:5}
.dash-title{left:0;right:0;top:30px;text-align:center;font-size:17px;font-weight:400;color:var(--ink)}
.search{left:11px;top:63px;width:338px;height:35px;background:var(--card);border-radius:4px;
  box-shadow:0 1px 4px rgba(0,0,0,.08);font-size:14px;padding:9px 10px;color:var(--ink)}
.search svg{position:absolute;right:10px;top:9px}
.dash-body{left:0;top:278px;width:360px;height:362px;background:var(--screen)}
.heading{font-size:18px;font-weight:400;color:var(--muted);z-index:2}
.cat{top:327px;width:144px;height:99px;border-radius:4px;overflow:hidden}
.cat__pill{position:absolute;left:23px;top:64px;width:96px;height:24px;border-radius:12px;background:#fff;
  font-size:13px;text-align:center;line-height:26px;color:var(--ink)}
.salon{top:477px;width:232px;height:160px;border-radius:4px;overflow:hidden;background:#fff}
.salon__img{position:absolute;left:0;top:0;width:100%;height:91px}
.salon__name{position:absolute;left:20px;top:93px;font-size:18px;font-weight:400;white-space:nowrap}
.badge{position:absolute;background:var(--teal);color:#fff;font-size:12px;text-align:center;border-radius:2px}
.salon__addr,.salon__tags{position:absolute;top:125px;font-size:10px;line-height:13px;color:var(--muted);white-space:nowrap}
/* menu screens */
.hero{left:0;top:0;width:360px;height:192px;background:linear-gradient(90deg,#b9c9c3 0,#d4d9d6 45%,#c9b7ae 75%,#d8c9c4 100%);opacity:.85}
.back{left:10px;top:34px;z-index:5}
.info{left:8px;top:145px;width:344px;height:57px;background:var(--card);box-shadow:0 2px 6px rgba(0,0,0,.05)}
.info__name{position:absolute;left:16px;top:9px;font-size:18px}
.info__addr{position:absolute;left:16px;top:34px;font-size:11.5px;color:var(--muted)}
.menu{left:10px;top:211px;width:340px;height:380px;background:#f8f7fc}
.menu__section{position:absolute;left:14px;font-size:12px;color:var(--muted);letter-spacing:.2px}
.row{position:absolute;left:13px;width:314px;height:52px}
.row__img{position:absolute;left:0;top:0;width:52px;height:52px;border-radius:50%}
.row__name{position:absolute;left:65px;top:16px;font-size:15px;color:var(--ink)}
.price{position:absolute;right:2px;top:11px;width:65px;height:30px;border:1px solid var(--line);border-radius:15px;
  font-size:15px;display:flex;align-items:center;justify-content:center;gap:5px;color:var(--ink)}
.footer{left:0;top:586px;width:360px;height:54px;background:#fff}
.footer__note{position:absolute;left:19px;top:19px;font-size:14px;color:var(--muted)}
.btn{position:absolute;background:var(--accent);color:#fff;font-size:14px;text-align:center;border-radius:2px}
.picker{left:0;top:484px;width:360px;height:156px;background:#fff;box-shadow:0 -2px 8px rgba(0,0,0,.05)}
.chip{position:absolute;border:1px solid var(--line);border-radius:15px;font-size:12.5px;text-align:center;color:var(--ink);background:#fff;white-space:nowrap}
.chip--day{top:20px;height:29px;width:58px;line-height:30px}
.chip--time{top:67px;height:26px;width:86px;line-height:27px;font-size:11.5px}
.chip--on{background:var(--accent);border-color:var(--accent);color:#fff}
</style>
</head>
<body>

<!-- Screen 1: Dashboard -->
<section class="phone phone--dashboard">
  <div class="status">
    <span class="status__left"><svg width="30" height="10"><rect x="0" y="6" width="2.5" height="4" fill="#111"/><rect x="3.5" y="4" width="2.5" height="6" fill="#111"/><rect x="7" y="2" width="2.5" height="8" fill="#111"/><rect x="10.5" y="0" width="2.5" height="10" fill="#111"/><path d="M17 4a7 7 0 0 1 10 0M19 6.5a4 4 0 0 1 6 0" stroke="#111" stroke-width="1.4" fill="none"/><circle cx="22" cy="9" r="1.2" fill="#111"/></svg></span>
    <span class="status__time">9:41 AM</span>
    <span class="status__right">100% <svg width="24" height="11"><rect x=".5" y=".5" width="21" height="10" rx="2" fill="none" stroke="#111"/><rect x="2" y="2" width="18" height="7" rx="1" fill="#111"/><rect x="22" y="3.5" width="1.5" height="4" fill="#111"/></svg></span>
  </div>
  <div class="abs dash-map" role="img" aria-label="Street map of the nearby area with salon location markers">
    <span class="marker" style="left:238px;top:131px"></span>
    <span class="marker" style="left:40px;top:163px"></span>
    <span class="marker marker--me" style="left:142px;top:204px"></span>
    <span class="marker" style="left:328px;top:187px;opacity:.6"></span>
    <span class="marker" style="left:29px;top:218px"></span>
    <span class="marker" style="left:272px;top:217px"></span>
    <span class="marker" style="left:152px;top:246px"></span>
  </div>
  <svg class="abs hamburger" width="18" height="13"><path d="M0 1h18M0 6.5h18M0 12h18" stroke="#333" stroke-width="1.6"/></svg>
  <div class="abs dash-title">Dashboard</div>
  <div class="avatar" role="img" aria-label="User profile photo"></div>
  <div class="abs search">New Delhi, India
    <svg width="17" height="17"><circle cx="7" cy="7" r="6" stroke="#666" stroke-width="1.5" fill="none"/><path d="M11.5 11.5L16 16" stroke="#666" stroke-width="1.5"/></svg>
  </div>
  <div class="abs dash-body"></div>
  <div class="abs heading" style="left:11px;top:292px">Categories</div>
  <svg class="abs" style="left:334px;top:296px" width="16" height="15"><path d="M0 3h16M0 11h16" stroke="#555" stroke-width="1.2"/><circle cx="11" cy="3" r="2.2" fill="#f2eff9" stroke="#555" stroke-width="1.2"/><circle cx="5" cy="11" r="2.2" fill="#f2eff9" stroke="#555" stroke-width="1.2"/></svg>

  <div class="abs cat" style="left:10px;background:linear-gradient(135deg,#6d7377,#b9b1a8 60%,#ddd6cf)" role="img" aria-label="Woman in a knit sweater, hair salon category">
    <div class="cat__pill">Hair Salon</div>
  </div>
  <div class="abs cat" style="left:164px;background:linear-gradient(135deg,#c9e6e7,#dfe6e4 50%,#b0624a)" role="img" aria-label="Woman with red hair, wax and spa category">
    <div class="cat__pill">Wax &amp; Spa</div>
  </div>
  <div class="abs cat" style="left:318px;width:50px;background:linear-gradient(135deg,#7c9a86,#c2cfc8)" role="img" aria-label="Outdoor salon category photo"></div>

  <div class="abs heading" style="left:11px;top:440px">Hair Salon</div>

  <article class="abs salon" style="left:10px">
    <div class="salon__img" style="background:linear-gradient(90deg,#8aa895,#c8c6bb 50%,#8d6a5a)" role="img" aria-label="Woman with curly hair outside the salon"></div>
    <div class="salon__name">Fern &amp; Finch Salon</div>
    <div class="badge" style="left:188px;top:96px;width:29px;height:19px;line-height:20px">4.7</div>
    <svg class="abs" style="left:19px;top:127px" width="8" height="11"><path d="M4 10.5C1 6.5 .5 5 .5 4a3.5 3.5 0 0 1 7 0c0 1-.5 2.5-3.5 6.5z" fill="#555"/><circle cx="4" cy="4" r="1.3" fill="#fff"/></svg>
    <div class="salon__addr" style="left:32px">48 Larkmoor Lane<br>London N7Q 2HT</div>
    <div class="salon__tags" style="left:140px">Hair, Spa, Salon<br>Wax, Others</div>
  </article>
  <article class="abs salon" style="left:253px">
    <div class="salon__img" style="background:linear-gradient(135deg,#cfe4e6,#e3e6e2 55%,#b26a4f)" role="img" aria-label="Woman with red hair in a salon"></div>
    <div class="salon__name">Salon Lumo</div>
    <svg class="abs" style="left:19px;top:127px" width="8" height="11"><path d="M4 10.5C1 6.5 .5 5 .5 4a3.5 3.5 0 0 1 7 0c0 1-.5 2.5-3.5 6.5z" fill="#555"/><circle cx="4" cy="4" r="1.3" fill="#fff"/></svg>
    <div class="salon__addr" style="left:32px">48 Larkmoor Lane<br>London N7Q 2HT</div>
  </article>
</section>

<!-- Screen 2: Salon menu -->
<section class="phone phone--menu">
  <div class="status">
    <span class="status__left"><svg width="30" height="10"><rect x="0" y="6" width="2.5" height="4" fill="#111"/><rect x="3.5" y="4" width="2.5" height="6" fill="#111"/><rect x="7" y="2" width="2.5" height="8" fill="#111"/><rect x="10.5" y="0" width="2.5" height="10" fill="#111"/><path d="M17 4a7 7 0 0 1 10 0M19 6.5a4 4 0 0 1 6 0" stroke="#111" stroke-width="1.4" fill="none"/><circle cx="22" cy="9" r="1.2" fill="#111"/></svg></span>
    <span class="status__time">9:41 AM</span>
    <span class="status__right">100% <svg width="24" height="11"><rect x=".5" y=".5" width="21" height="10" rx="2" fill="none" stroke="#111"/><rect x="2" y="2" width="18" height="7" rx="1" fill="#111"/><rect x="22" y="3.5" width="1.5" height="4" fill="#111"/></svg></span>
  </div>
  <div class="abs hero" role="img" aria-label="Faded cover photo of a woman with curly hair outside the salon"></div>
  <svg class="abs back" width="20" height="16"><path d="M19 8H2M8 1L1 8l7 7" stroke="#222" stroke-width="1.6" fill="none"/></svg>
  <div class="avatar" role="img" aria-label="User profile photo"></div>
  <div class="abs info">
    <div class="info__name">Fern &amp; Finch Salon</div>
    <div class="info__addr">48 Larkmoor Lane London N7Q 2HT</div>
    <svg class="abs" style="left:288px;top:20px" width="14" height="14"><path d="M7 0l2.1 4.5 4.9.5-3.7 3.3 1.1 4.8L7 10.6 2.6 13.1l1.1-4.8L0 5l4.9-.5z" fill="var(--star)"/></svg>
    <div class="badge" style="left:309px;top:19px;width:28px;height:18px;line-height:19px">4.7</div>
  </div>
  <div class="abs menu">
    <div class="menu__section" style="top:16px">HAIR CARE</div>
    <div class="row" style="top:37px"><div class="row__img" style="background:radial-gradient(circle,#a9825f,#4b3526)" role="img" aria-label="Hair straightening photo"></div><div class="row__name">Hair straightening</div><div class="price">+ <span>$24</span></div></div>
    <div class="row" style="top:103px"><div class="row__img" style="background:radial-gradient(circle,#9a7a68,#3a2a22)" role="img" aria-label="Hair curling photo"></div><div class="row__name">Hair Curling</div><div class="price">+ <span>$44</span></div></div>
    <div class="row" style="top:170px"><div class="row__img" style="background:radial-gradient(circle,#f1ede6,#cbb9a4)" role="img" aria-label="Waxing photo"></div><div class="row__name">Waxing</div><div class="price">+ <span>$54</span></div></div>
    <div class="menu__section" style="top:236px">FACIAL</div>
    <div class="row" style="top:255px"><div class="row__img" style="background:radial-gradient(circle,#7b6458,#22201f)" role="img" aria-label="Facial pack photo"></div><div class="row__name">Facial Pack</div><div class="price">+ <span>$24</span></div></div>
    <div class="row" style="top:322px"><div class="row__img" style="background:radial-gradient(circle,#d9b48f,#9fc4cf)" role="img" aria-label="Hair curling with flower crown photo"></div><div class="row__name">Hair Curling</div><div class="price">+ <span>$44</span></div></div>
  </div>
  <div class="abs footer">
    <div class="footer__note">No Bookings to Show</div>
    <div class="btn" style="left:219px;top:9px;width:132px;height:38px;line-height:40px">Book Now</div>
  </div>
</section>

<!-- Screen 3: Booking slot picker -->
<section class="phone phone--booking">
  <div class="status">
    <span class="status__left"><svg width="30" height="10"><rect x="0" y="6" width="2.5" height="4" fill="#111"/><rect x="3.5" y="4" width="2.5" height="6" fill="#111"/><rect x="7" y="2" width="2.5" height="8" fill="#111"/><rect x="10.5" y="0" width="2.5" height="10" fill="#111"/><path d="M17 4a7 7 0 0 1 10 0M19 6.5a4 4 0 0 1 6 0" stroke="#111" stroke-width="1.4" fill="none"/><circle cx="22" cy="9" r="1.2" fill="#111"/></svg></span>
    <span class="status__time">9:41 AM</span>
    <span class="status__right">100% <svg width="24" height="11"><rect x=".5" y=".5" width="21" height="10" rx="2" fill="none" stroke="#111"/><rect x="2" y="2" width="18" height="7" rx="1" fill="#111"/><rect x="22" y="3.5" width="1.5" height="4" fill="#111"/></svg></span>
  </div>
  <div class="abs hero" role="img" aria-label="Faded cover photo of a woman with curly hair outside the salon" style="background:linear-gradient(90deg,#b3cdc7 0,#d2dcd8 45%,#c3c9c3 75%,#d5d6d0 100%)"></div>
  <svg class="abs back" width="20" height="16"><path d="M19 8H2M8 1L1 8l7 7" stroke="#222" stroke-width="1.6" fill="none"/></svg>
  <div class="avatar" role="img" aria-label="User profile photo"></div>
  <div class="abs info">
    <div class="info__name">Fern &amp; Finch Salon</div>
    <div class="info__addr">48 Larkmoor Lane London N7Q 2HT</div>
    <svg class="abs" style="left:288px;top:20px" width="14" height="14"><path d="M7 0l2.1 4.5 4.9.5-3.7 3.3 1.1 4.8L7 10.6 2.6 13.1l1.1-4.8L0 5l4.9-.5z" fill="var(--star)"/></svg>
    <div class="badge" style="left:309px;top:19px;width:28px;height:18px;line-height:19px">4.7</div>
  </div>
  <div class="abs menu">
    <div class="menu__section" style="top:16px">HAIR CARE</div>
    <div class="row" style="top:37px"><div class="row__img" style="background:radial-gradient(circle,#a9825f,#4b3526)" role="img" aria-label="Hair straightening photo"></div><div class="row__name">Hair straightening</div><div class="price">+ <span>$24</span></div></div>
    <div class="row" style="top:103px"><div class="row__img" style="background:radial-gradient(circle,#9a7a68,#3a2a22)" role="img" aria-label="Hair curling photo"></div><div class="row__name">Hair Curling</div><div class="price">+ <span>$44</span></div></div>
    <div class="row" style="top:170px"><div class="row__img" style="background:radial-gradient(circle,#f1ede6,#cbb9a4)" role="img" aria-label="Waxing photo"></div><div class="row__name">Waxing</div><div class="price">+ <span>$54</span></div></div>
    <div class="menu__section" style="top:236px">FACIAL</div>
    <div class="row" style="top:255px"><div class="row__img" style="background:radial-gradient(circle,#7b6458,#22201f)" role="img" aria-label="Facial pack photo"></div></div>
  </div>
  <div class="abs picker">
    <div class="chip chip--day" style="left:10px">Sat 30</div>
    <div class="chip chip--day" style="left:77px">Sun 31</div>
    <div class="chip chip--day chip--on" style="left:143px">Mon 30</div>
    <div class="chip chip--day" style="left:210px">Tue 31</div>
    <div class="chip chip--day" style="left:276px">Wed 30</div>
    <div class="chip chip--day" style="left:342px">Thu 1</div>
    <div class="chip chip--time" style="left:2px;width:76px">11:00 - 12:00</div>
    <div class="chip chip--time chip--on" style="left:85px">12:00 - 01:00</div>
    <div class="chip chip--time" style="left:178px">01:00 - 02:00</div>
    <div class="chip chip--time" style="left:271px">03:00 - 04:00</div>
    <div class="btn" style="left:10px;top:110px;width:340px;height:38px;line-height:40px">Book Now</div>
  </div>
</section>

</body>
</html>
```